Flyer-Design für Yoga-Studio
Zielgruppe
Yoga-Studio, Zielgruppe: alle Erwachsenen
Aufgabenstellung
Der Flyer soll nicht feminin wirken, eher in Grau-Blau oder Braun Tönen. Nicht überladen oder verschnörkelt. Es darf gerne ein Symbol darin vorkommen. Gerne DinA6 (Hinter und Forderseite)
Der Flyer ist für die Neueröffnung eines Yogastudios, alle wichtigen Infos sollen enthalten sein.

```html
<!DOCTYPE html>
<html lang="de">
<head>
<meta charset="utf-8">
<title>Sama Yoga – Flyer Vorder- und Rückseite</title>
<link rel="stylesheet" href="https://fonts.googleapis.com/css2?family=Oswald:wght@300;600&family=Pathway+Gothic+One&display=swap">
<style>
  :root{
    --board:#5c5c5c;
    --sky:#1d8cbc;
    --mist:#2f6f9c;
    --forest:#0d2a55;
    --night:#03081a;
    --white:#ffffff;
    --ink:#3a3a3a;
    --accent:#12a9df;
    --rule:rgba(255,255,255,.75);
  }
  *{margin:0;padding:0;box-sizing:border-box}
  html,body{width:1200px;height:833px;overflow:hidden;background:var(--board)}
  body{position:relative;font-family:"Pathway Gothic One",sans-serif;color:var(--white)}
  .flyer{position:absolute;top:62px;width:487px;height:689px;overflow:hidden;box-shadow:4px 4px 6px rgba(0,0,0,.35)}
  .flyer--front{left:66px}
  .flyer--back{left:595px}
  .photo{position:absolute;inset:0;
    background:
      radial-gradient(ellipse at 30% 18%, rgba(170,215,235,.45), transparent 55%),
      linear-gradient(180deg,var(--sky) 0%,var(--mist) 35%,var(--forest) 68%,var(--night) 100%);}
  .frame{position:absolute;border:1px solid var(--rule)}
  .flyer--front .frame{left:14px;top:14px;width:456px;height:660px}
  .flyer--back .frame{left:17px;top:22px;width:451px;height:652px}
  .t{position:absolute;white-space:nowrap;line-height:1}
  .brand-small{font-family:"Oswald",sans-serif;font-weight:300;font-size:33px;letter-spacing:1px}
  .brand-big{font-family:"Oswald",sans-serif;font-weight:600;font-size:82px;letter-spacing:-1px;transform:scaleX(.86);transform-origin:right}
  .rule{position:absolute;height:1px;background:var(--rule)}
  .dot{position:absolute;width:3px;height:3px;border-radius:50%;background:var(--white)}
  .sc{font-variant:small-caps}
  .right{text-align:right}
  .band{position:absolute;background:var(--white);color:var(--ink)}
  .center{left:0;right:0;text-align:center}
  .social{display:inline-flex;align-items:center;gap:4px;margin-left:6px}
  .social i{display:inline-block;width:9px;height:9px;background:var(--white)}
</style>
</head>
<body>

<section class="flyer flyer--front">
  <div class="photo" role="img" aria-label="Foto: Hand in Meditationshaltung über nebligem blauem Nadelwald"></div>
  <div class="frame"></div>

  <div class="t brand-small" style="right:44px;top:42px">SAMA</div>
  <div class="t brand-big" style="right:44px;top:72px">YOGA</div>
  <div class="rule" style="left:286px;width:162px;top:177px"></div>
  <div class="t" style="right:40px;top:187px;font-size:20px">HATHA YOGA · ASHTANGA YOGA · PRANAJAMAS</div>

  <div class="t" style="left:88px;top:268px;font-size:21px">HATHA YOGA</div>
  <div class="t sc right" style="right:40px;top:268px;font-size:21px">Montag bis Freitag</div>
  <div class="t right" style="right:40px;top:296px;font-size:20px">6.45 - 7.45 <span class="sc">Uhr</span></div>

  <div class="t" style="left:88px;top:345px;font-size:21px">ASHTANGA YOGA</div>
  <div class="t sc right" style="right:40px;top:345px;font-size:21px">Montag, Dienstag und Donnerstag</div>
  <div class="t right" style="right:40px;top:373px;font-size:20px">8.30 - 10 <span class="sc">Uhr</span></div>

  <div class="t" style="left:88px;top:421px;font-size:21px">PRANAJAMAS</div>
  <div class="t sc right" style="right:40px;top:421px;font-size:21px">Auf Anfrage</div>

  <div class="band" style="left:14px;width:456px;top:474px;height:90px">
    <div class="t sc center" style="top:9px;font-size:20px">Jeden Mittwoch 17-18.30 Uhr</div>
    <div class="t sc center" style="top:32px;font-size:26px;color:var(--accent)">Gratis Yoga</div>
    <div class="t sc center" style="top:61px;font-size:17px">(Hatha oder Ashtanga)</div>
  </div>

  <div class="t sc center" style="top:579px;font-size:18px">Interessiert ? Anmeldungen (auch Probelektionen) oder Fragen</div>
  <div class="t sc center" style="top:602px;font-size:18px">Whatsapp an Marco 076 000 12 34</div>
  <div class="t sc center" style="top:627px;font-size:18px">Follow us on<span class="social"><i></i>Bildnetz <i></i>Kurzpost</span></div>
</section>

<section class="flyer flyer--back">
  <div class="photo" role="img" aria-label="Foto: Hand in Meditationshaltung über nebligem blauem Nadelwald"></div>
  <div class="frame"></div>

  <div class="t brand-small" style="right:48px;top:40px">SAMA</div>
  <div class="t brand-big" style="right:48px;top:72px">YOGA</div>
  <div class="rule" style="left:283px;width:160px;top:184px"></div>
  <div class="dot" style="left:244px;top:201px"></div>
  <div class="dot" style="left:353px;top:201px"></div>

  <div class="t" style="left:71px;top:212px;font-size:24px">MORGEN YOGA</div>

  <div class="band" style="left:17px;width:451px;top:249px;height:37px">
    <div class="t sc" style="left:54px;top:8px;font-size:21px">Wach - Energiegeladen - Ausgeglichen in den Tag starten</div>
  </div>

  <div class="t sc" style="left:71px;top:319px;font-size:26px">Montag - Freitag 6.45 - 7.45 Uhr</div>
  <div class="t sc" style="left:71px;top:354px;font-size:26px">Lindenweg 14, 0000 Musterstadt</div>

  <div class="t sc center" style="top:581px;font-size:18px">Interessiert ? Anmeldungen (auch Probelektionen) oder Fragen</div>
  <div class="t sc center" style="top:604px;font-size:18px">Whatsapp an Marco 076 000 12 34</div>
  <div class="t sc center" style="top:628px;font-size:18px">Follow us on<span class="social"><i></i>Bildnetz <i></i>Kurzpost</span></div>
</section>

</body>
</html>
```